MODERN DESIGN BUSINESS CARDS FOR A CREDIT REPAIR COMPANY

Our goal is to have a modern yet professional business card for our credit repair company. Something that'll catch the eye of our clients. PLEASE BE CREATIVE. WE WOULD LIKE TO SEE HOW THIS WOULD LOOK WITH A WHITE AND BLACK BACK GROUND.

Contact Information for Business Card

THIS WILL BE A DOUBLE SIDED BUSINESS CARD, THE COLORS WE WOULD LIKE TO HAVE IS BLACK, BLUES AND WHITE

Colors
3277b5
33a6d7
ffffff

Requirements
Must have
• MUST HAVE OUR LOGO, BUSINESS PHONE # (482 )607-5731, EXAMPLESOCIAL LINK EXAMPLESOCIAL.TEST/VORMANTHCREDITSOLUTIONS, CALL US FOR YOUR FREE CONSULTATION
Nice to have
• ITEMS WE DELETE: LATE PAYMENTS, CHARGE-OFFS, REPOSESSIONS, HOSPITAL BILLS, STUDENT LOANS, FORECLOSURES, CHILD SUPPORT AND BANKRUPTCIES.

```html
<!DOCTYPE html>
<html lang="en">
<head>
<meta charset="utf-8">
<title>Vormanth Credit Solutions — Business Card</title>
<link rel="stylesheet" href="https://fonts.googleapis.com/css2?family=Montserrat:wght@400;500;600;700;800&display=swap">
<style>
  :root {
    --bg: #e4e4e2;
    --paper: #ffffff;
    --navy: #1a4a8c;
    --navy-deep: #0d3672;
    --navy-dark: #0a2c60;
    --ink: #3a3a3c;
    --grey: #5c5c60;
    --white: #ffffff;
    --faint: rgba(255,255,255,0.10);
  }
  * { margin: 0; padding: 0; box-sizing: border-box; }
  html, body { width: 1200px; height: 801px; overflow: hidden; }
  body {
    background: var(--bg);
    font-family: "Montserrat", sans-serif;
    position: relative;
  }
  .card {
    position: absolute;
    top: 246px;
    width: 540px;
    height: 309px;
    overflow: hidden;
    box-shadow: 0 6px 18px rgba(0,0,0,0.18);
  }
  /* Front */
  .card-front { left: 50px; background: var(--paper); }
  .front-logo {
    position: absolute; left: 44px; top: 190px;
    display: flex; align-items: center; gap: 12px;
  }
  .logo-dot {
    width: 46px; height: 46px; border-radius: 50%;
    border: 5px solid var(--navy);
  }
  .logo-name {
    font-weight: 700; color: var(--navy); line-height: 1;
  }
  .logo-name .big { display: block; font-size: 30px; letter-spacing: 0.5px; }
  .logo-name .small { display: block; font-size: 9.5px; letter-spacing: 4.2px; margin-top: 5px; }
  .front-divider {
    position: absolute; left: 292px; top: 110px;
    width: 1.5px; height: 120px; background: var(--navy);
  }
  .contact {
    position: absolute; left: 312px; top: 96px;
  }
  .contact-name { font-size: 20px; font-weight: 800; color: var(--navy); letter-spacing: 0.3px; }
  .contact-title { font-size: 14px; font-weight: 600; color: var(--ink); margin-top: 2px; }
  .contact-line {
    display: flex; align-items: center; gap: 8px;
    font-size: 13.5px; font-weight: 500; color: var(--grey);
    margin-top: 10px;
  }
  .contact-line + .contact-line { margin-top: 4px; }
  .contact-icon { width: 16px; height: 16px; flex: none; }
  .social-square { width: 14px; height: 14px; background: var(--navy); border-radius: 2px; flex: none; margin: 0 1px; }
  .badge {
    position: absolute; right: 34px; top: 24px;
    width: 62px; height: 62px; border-radius: 50%;
    background: radial-gradient(circle, #3d7ad0 0 55%, #1c1c22 56% 100%);
  }

  /* Back */
  .card-back {
    left: 610px;
    background: linear-gradient(160deg, var(--navy) 0%, var(--navy-deep) 60%, var(--navy-dark) 100%);
    color: var(--white);
  }
  .back-decoration {
    position: absolute; right: -40px; top: 40px;
    width: 240px; height: 240px; border-radius: 50%;
    border: 26px solid var(--faint);
  }
  .back-logo {
    position: absolute; left: 40px; top: 34px;
    display: flex; align-items: center; gap: 14px;
  }
  .back-logo .logo-dot { border-color: var(--white); width: 52px; height: 52px; }
  .back-logo .logo-name { color: var(--white); }
  .back-logo .logo-name .big { font-size: 40px; }
  .back-logo .logo-name .small { font-size: 12px; letter-spacing: 6px; }
  .delete-list {
    position: absolute; left: 108px; top: 128px;
    list-style: none; font-weight: 600; font-size: 13px; letter-spacing: 0.4px;
  }
  .delete-list .heading { font-size: 15px; margin-bottom: 3px; }
  .delete-list li { display: flex; align-items: center; gap: 7px; line-height: 18px; }
  .trash { width: 12px; height: 13px; flex: none; }
</style>
</head>
<body>

<section class="card card-front" aria-label="Card front">
  <div class="front-logo">
    <span class="logo-dot"></span>
    <span class="logo-name"><span class="big">VORMANTH</span><span class="small">CREDIT SOLUTIONS</span></span>
  </div>
  <div class="front-divider"></div>
  <div class="contact">
    <p class="contact-name">MARCUS DELAVALE</p>
    <p class="contact-title">Managing Director</p>
    <p class="contact-line">
      <svg class="contact-icon" viewBox="0 0 24 24"><path fill="#1a4a8c" d="M3 7c0-2 3-4 9-4s9 2 9 4v2h-5V7H8v2H3z M6 11h12l2 9H4z"/><circle cx="12" cy="15" r="2.2" fill="#fff"/></svg>
      (482 )607-5731
    </p>
    <p class="contact-line"><span class="social-square"></span>vormanthcreditsolutions</p>
  </div>
  <div class="badge" role="img" aria-label="Certification badge"></div>
</section>

<section class="card card-back" aria-label="Card back">
  <div class="back-decoration"></div>
  <div class="back-logo">
    <span class="logo-dot"></span>
    <span class="logo-name"><span class="big">VORMANTH</span><span class="small">CREDIT SOLUTIONS</span></span>
  </div>
  <ul class="delete-list">
    <li class="heading">ITEMS WE DELETE</li>
    <li><svg class="trash" viewBox="0 0 12 13"><path d="M1 2.5h10M4.5 2.5V1h3v1.5M2.2 2.5l.8 10h6l.8-10" fill="none" stroke="#fff" stroke-width="1.2"/></svg>LATE PAYMENTS</li>
    <li><svg class="trash" viewBox="0 0 12 13"><path d="M1 2.5h10M4.5 2.5V1h3v1.5M2.2 2.5l.8 10h6l.8-10" fill="none" stroke="#fff" stroke-width="1.2"/></svg>CHARGE-OFFS</li>
    <li><svg class="trash" viewBox="0 0 12 13"><path d="M1 2.5h10M4.5 2.5V1h3v1.5M2.2 2.5l.8 10h6l.8-10" fill="none" stroke="#fff" stroke-width="1.2"/></svg>REPOSESSIONS</li>
    <li><svg class="trash" viewBox="0 0 12 13"><path d="M1 2.5h10M4.5 2.5V1h3v1.5M2.2 2.5l.8 10h6l.8-10" fill="none" stroke="#fff" stroke-width="1.2"/></svg>HOSPITAL BILLS</li>
    <li><svg class="trash" viewBox="0 0 12 13"><path d="M1 2.5h10M4.5 2.5V1h3v1.5M2.2 2.5l.8 10h6l.8-10" fill="none" stroke="#fff" stroke-width="1.2"/></svg>STUDENT LOANS</li>
    <li><svg class="trash" viewBox="0 0 12 13"><path d="M1 2.5h10M4.5 2.5V1h3v1.5M2.2 2.5l.8 10h6l.8-10" fill="none" stroke="#fff" stroke-width="1.2"/></svg>FORECLOSURES,</li>
    <li><svg class="trash" viewBox="0 0 12 13"><path d="M1 2.5h10M4.5 2.5V1h3v1.5M2.2 2.5l.8 10h6l.8-10" fill="none" stroke="#fff" stroke-width="1.2"/></svg>CHILD SUPPORT AND BANKRUPTCIES</li>
  </ul>
</section>

</body>
</html>
```